Quillo Flash Banner Ad

We require a flash banner ad for a new product of ours called Quillo (www.quillo.com.au). Quillo is a web-based system generating life insurance quotes using a widget embedded in your site.
The banner should have the following screens:
1. Life Insurance, Total & Permanent Disablement Insurance, Income Protection Insurance
2. No Blood Tests or Medicals Required.
3. Up to $1 million Cover with Leading Brands.
4. Click here for an Instant Quote.
We require the following sizes:
- 300 x 250
- 728 x 90
Industry/Entity Type
Life Insurance
Look and feel
Each slider illustrates characteristics of the customer's brand and the style your logo design should communicate.

```html
<!DOCTYPE html>
<html lang="en">
<head>
<meta charset="utf-8">
<title>Quillo Flash Banner Ad</title>
<link rel="stylesheet" href="https://fonts.googleapis.com/css2?family=Arimo:wght@400;700&display=swap">
<style>
  :root {
    --teal-deep: #195a69;
    --teal-mid: #5f919a;
    --mist: #dce6e8;
    --band-top: #2d6c77;
    --band-bottom: #6a9b98;
    --ad-top: #1b5b6a;
    --ad-bottom: #6d9ca5;
    --white: #ffffff;
    --green: #6ab64c;
  }
  * { margin: 0; padding: 0; box-sizing: border-box; }
  html, body { width: 1200px; height: 900px; overflow: hidden; }
  body {
    position: relative;
    font-family: "Arimo", Arial, sans-serif;
    color: var(--white);
    background: linear-gradient(180deg, var(--teal-deep) 0%, var(--teal-mid) 45%, var(--mist) 84%);
  }
  .ad {
    position: absolute;
    background: linear-gradient(180deg, var(--ad-top) 0%, var(--ad-bottom) 100%);
    outline: 3px dashed var(--white);
    outline-offset: 0;
  }
  .ad-square { left: 449px; top: 186px; width: 300px; height: 248px; }
  .ad-leader { left: 235px; top: 525px; width: 728px; height: 91px; }
  .replay {
    position: absolute; right: 10px; top: 9px;
    font-size: 11px; font-weight: 700;
  }
  .headline { font-size: 44px; font-weight: 700; line-height: 1; letter-spacing: 0.3px; }
  .subline { font-size: 18px; font-weight: 700; line-height: 1; }
  .ad-square .headline { position: absolute; top: 61px; width: 100%; text-align: center; }
  .ad-square .subline { position: absolute; top: 111px; width: 100%; text-align: center; }
  .ad-leader .headline { position: absolute; left: 25px; top: 29px; }
  .ad-leader .subline { position: absolute; left: 273px; top: 47px; }
  .brand {
    position: absolute;
    display: flex; align-items: center; gap: 10px;
    font-size: 40px; font-weight: 700; color: var(--green);
  }
  .brand-mark { width: 20px; height: 20px; background: var(--green); }
  .ad-square .brand { left: 50%; top: 152px; transform: translateX(-50%); }
  .ad-leader .brand { left: 540px; top: 22px; }
  .footer-band {
    position: absolute; left: 0; bottom: 0; width: 1200px; height: 145px;
    background: linear-gradient(180deg, var(--band-top) 0%, var(--band-bottom) 100%);
    display: flex; align-items: center; justify-content: center;
  }
  .footer-url { font-size: 42px; font-weight: 700; letter-spacing: 0.2px; }
</style>
</head>
<body>
  <section class="ad ad-square" aria-label="300 by 250 banner">
    <span class="replay">Replay</span>
    <p class="headline">Click Here</p>
    <p class="subline">for an Instant Quote.</p>
    <div class="brand"><span class="brand-mark"></span>Quillo</div>
  </section>

  <section class="ad ad-leader" aria-label="728 by 90 banner">
    <p class="headline">Click Here</p>
    <p class="subline">for an Instant Quote.</p>
    <div class="brand"><span class="brand-mark"></span>Quillo</div>
  </section>

  <footer class="footer-band">
    <p class="footer-url">www.pinecrest-studio.com/hosted/quillo</p>
  </footer>
</body>
</html>
```